Company producing high tech raw materials for the bakery industry needs new packaging design

We need a new design for the bag containing our products.

We are a producer of chemical and high tech raw materials for the bakery and confectionery sectors (we have small customers & also large industrial customers).

Our profile is in between food and pharmaceuticals. So the new design needs to present foremostly seriousness and reliability, but still not being blunt and boring as it contains exciting cutting edge food technology ingredients.

We have 3 different sizes of bags to contain our products, (which is in the form of powder like flour). 650x400x130 for 10 kgs, 700x460x130 for 15 kgs, 900x500x130 for 25 kgs, so the design should look good in all three sizes. Bags are from thick paper.

I am attaching pictures of our current (very badly designed blue-grey) bag and some pictures of competition bags, so that you get an idea of how the bags in the industry generally are.

The new bag should contain the logo (attached). The colors used in the logo are CMYK , DARK BLUE 100,83,5,27 LIGHT BLUE 60,40,0,0. Our primary colors are like the ones in the logo and as secondary we have grey and yellow (orange). Maximum number of different colors that can be used in the new design is 4 (because the printing cost is much more expensive with more than that).

FYI on the bag, as you can see in the attached pictures of our current bag, must be an A5 - A4 size label and the top opening is sewed.

Please do not hesitate to contact us for any further questions or clarification.

Requirements
Must have
• Take into account the label and the closing on top of the bag
3 bag sizes
Highly visible logo

```html
<!DOCTYPE html>
<html lang="en">
<head>
<meta charset="utf-8">
<title>Norvel bakery ingredient bags</title>
<link rel="stylesheet" href="https://fonts.googleapis.com/css2?family=Montserrat:wght@600&family=Open+Sans:wght@400;600;700&display=swap">
<style>
  :root {
    --stage: #e6e6e6;
    --navy: #213a78;
    --sky: #6a87c6;
    --paper: #ffffff;
    --leaf-a: #8ccdbd;
    --leaf-b: #c9ddd6;
    --ink: #1d2230;
  }
  * { box-sizing: border-box; margin: 0; padding: 0; }
  html, body { width: 1200px; height: 771px; overflow: hidden; background: var(--stage); }
  .stage { position: relative; width: 1200px; height: 771px; }

  .bag { position: absolute; overflow: hidden; background: var(--paper); }
  .bag-shape { position: absolute; inset: 0; width: 100%; height: 100%; }

  .mark { position: absolute; border-radius: 50%; background: var(--sky); }
  .brand-name {
    position: absolute; left: 0; right: 0; text-align: center;
    font-family: "Montserrat", sans-serif; font-weight: 600; line-height: 1;
    color: var(--navy); letter-spacing: 0.5px;
  }
  .brand-tagline {
    position: absolute; left: 0; right: 0; text-align: center;
    font-family: "Open Sans", sans-serif; font-weight: 400; line-height: 1;
    color: var(--sky); letter-spacing: 3px;
  }

  .product-label {
    position: absolute; background: var(--paper); padding: 3.5% 4.5%;
    font-family: "Open Sans", sans-serif; color: var(--ink);
  }
  .label-table {
    display: grid; width: 100%; height: 100%;
    grid-template-columns: 23% 52% 25%;
    grid-template-rows: 12% 4% 15% 25% 25% 19%;
    border: 0.6px solid var(--ink);
  }
  .label-title {
    grid-column: 1 / 4; background: var(--sky); color: var(--paper);
    display: flex; align-items: center; justify-content: center;
    font-size: 2.4em; font-weight: 400; letter-spacing: 0.3px;
  }
  .label-subtitle {
    grid-column: 1 / 4; background: var(--navy); color: var(--paper);
    display: flex; align-items: center; justify-content: center;
    font-size: 0.75em; font-weight: 700; text-transform: uppercase;
  }
  .cell {
    border-top: 0.6px solid var(--ink); padding: 0 4%;
    display: flex; align-items: center; font-size: 0.7em; line-height: 1.3;
  }
  .cell-key { font-weight: 700; text-transform: uppercase; border-right: 0.6px solid var(--ink); }
  .cell-text { grid-column: 2 / 4; }
  .cell-wide { grid-column: 1 / 3; flex-direction: column; align-items: flex-start; justify-content: center; border-right: 0.6px solid var(--ink); }
  .cell-wide .caps { text-transform: uppercase; font-weight: 600; }
  .cell-weight { justify-content: center; font-size: 3em; font-weight: 700; }

  .bag-small  { left: 88px;  top: 244px; width: 269px; height: 432px; }
  .bag-medium { left: 417px; top: 214px; width: 304px; height: 462px; }
  .bag-large  { left: 783px; top: 91px;  width: 329px; height: 590px; }
</style>
</head>
<body>
<main class="stage">

  <section class="bag bag-small">
    <svg class="bag-shape" viewBox="0 0 269 432" preserveAspectRatio="none">
      <defs>
        <linearGradient id="leaf-small" x1="0" y1="0" x2="1" y2="1">
          <stop offset="0" stop-color="var(--leaf-b)"/>
          <stop offset="0.5" stop-color="var(--leaf-a)"/>
          <stop offset="1" stop-color="var(--leaf-b)"/>
        </linearGradient>
      </defs>
      <rect class="closure-band" x="0" y="0" width="269" height="26" fill="var(--navy)"/>
      <path class="leaf-field" role="img" aria-label="Pattern of outlined teal and grey leaves" d="M0,223 Q134.5,321 269,223 L269,432 L0,432 Z" fill="url(#leaf-small)"/>
      <path class="base-band" d="M0,396 L134.5,372 L269,396 L269,432 L0,432 Z" fill="var(--navy)"/>
    </svg>
    <div class="mark" style="left:107px;top:63px;width:48px;height:48px"></div>
    <div class="brand-name" style="top:148px;font-size:50px">Norvel</div>
    <div class="brand-tagline" style="top:197px;font-size:16px">ΑΦΟΙ ΚΑΛΛΙΔΗ</div>
    <div class="product-label" style="left:50px;top:278px;width:175px;height:124px;font-size:3.6px">
      <div class="label-table">
        <div class="label-title">FARINEL K240</div>
        <div class="label-subtitle">Bakery improver for professional dough</div>
        <div class="cell cell-key">Usage</div>
        <div class="cell cell-text">Add to flour at two percent of total weight and mix well.</div>
        <div class="cell cell-key">Storage</div>
        <div class="cell cell-text">Keep dry and cool below twenty five degrees, sealed after opening.</div>
        <div class="cell cell-wide"><span class="caps">Batch and best before see stitching</span><span class="caps">Ingredients: wheat flour, enzymes, emulsifier E472e, ascorbic acid, calcium phosphate.</span></div>
        <div class="cell cell-weight">10 kg</div>
        <div class="cell cell-wide">Produced in Greece for professional bakery use only.</div>
        <div class="cell"></div>
      </div>
    </div>
  </section>

  <section class="bag bag-medium">
    <svg class="bag-shape" viewBox="0 0 304 462" preserveAspectRatio="none">
      <defs>
        <linearGradient id="leaf-medium" x1="0" y1="0" x2="1" y2="1">
          <stop offset="0" stop-color="var(--leaf-b)"/>
          <stop offset="0.5" stop-color="var(--leaf-a)"/>
          <stop offset="1" stop-color="var(--leaf-b)"/>
        </linearGradient>
      </defs>
      <rect class="closure-band" x="0" y="0" width="304" height="26" fill="var(--navy)"/>
      <path class="leaf-field" role="img" aria-label="Pattern of outlined teal and grey leaves" d="M0,224 Q152,338 304,224 L304,462 L0,462 Z" fill="url(#leaf-medium)"/>
      <path class="base-band" d="M0,441 L152,402 L304,441 L304,462 L0,462 Z" fill="var(--navy)"/>
    </svg>
    <div class="mark" style="left:126px;top:63px;width:54px;height:54px"></div>
    <div class="brand-name" style="top:154px;font-size:50px">Norvel</div>
    <div class="brand-tagline" style="top:201px;font-size:16px">ΑΦΟΙ ΚΑΛΛΙΔΗ</div>
    <div class="product-label" style="left:64px;top:295px;width:178px;height:125px;font-size:3.6px">
      <div class="label-table">
        <div class="label-title">FARINEL K240</div>
        <div class="label-subtitle">Bakery improver for professional dough</div>
        <div class="cell cell-key">Usage</div>
        <div class="cell cell-text">Add to flour at two percent of total weight and mix well.</div>
        <div class="cell cell-key">Storage</div>
        <div class="cell cell-text">Keep dry and cool below twenty five degrees, sealed after opening.</div>
        <div class="cell cell-wide"><span class="caps">Batch and best before see stitching</span><span class="caps">Ingredients: wheat flour, enzymes, emulsifier E472e, ascorbic acid, calcium phosphate.</span></div>
        <div class="cell cell-weight">15 kg</div>
        <div class="cell cell-wide">Produced in Greece for professional bakery use only.</div>
        <div class="cell"></div>
      </div>
    </div>
  </section>

  <section class="bag bag-large">
    <svg class="bag-shape" viewBox="0 0 329 590" preserveAspectRatio="none">
      <defs>
        <linearGradient id="leaf-large" x1="0" y1="0" x2="1" y2="1">
          <stop offset="0" stop-color="var(--leaf-b)"/>
          <stop offset="0.5" stop-color="var(--leaf-a)"/>
          <stop offset="1" stop-color="var(--leaf-b)"/>
        </linearGradient>
      </defs>
      <rect class="closure-band" x="0" y="0" width="329" height="26" fill="var(--navy)"/>
      <path class="leaf-field" role="img" aria-label="Pattern of outlined teal and grey leaves" d="M0,322 Q164.5,414 329,322 L329,590 L0,590 Z" fill="url(#leaf-large)"/>
      <path class="base-band" d="M0,565 L164.5,534 L329,565 L329,590 L0,590 Z" fill="var(--navy)"/>
    </svg>
    <div class="mark" style="left:132px;top:117px;width:64px;height:64px"></div>
    <div class="brand-name" style="top:223px;font-size:62px">Norvel</div>
    <div class="brand-tagline" style="top:286px;font-size:20px">ΑΦΟΙ ΚΑΛΛΙΔΗ</div>
    <div class="product-label" style="left:60px;top:394px;width:208px;height:149px;font-size:4.2px">
      <div class="label-table">
        <div class="label-title">FARINEL K240</div>
        <div class="label-subtitle">Bakery improver for professional dough</div>
        <div class="cell cell-key">Usage</div>
        <div class="cell cell-text">Add to flour at two percent of total weight and mix well.</div>
        <div class="cell cell-key">Storage</div>
        <div class="cell cell-text">Keep dry and cool below twenty five degrees, sealed after opening.</div>
        <div class="cell cell-wide"><span class="caps">Batch and best before see stitching</span><span class="caps">Ingredients: wheat flour, enzymes, emulsifier E472e, ascorbic acid, calcium phosphate.</span></div>
        <div class="cell cell-weight">25 kg</div>
        <div class="cell cell-wide">Produced in Greece for professional bakery use only.</div>
        <div class="cell"></div>
      </div>
    </div>
  </section>

</main>
</body>
</html>
```